Business Card Design Project

it should have the logo in one side
the other side

Name
Position
telephone
email

Target Market(s)

Business prospects and upscale Fashion shoppers

Industry/Entity Type

Business

Font styles to use
Serif
Sans Serif

Requirements
Must have
• very elegant, upscale, modern
Nice to have
• layering, embossed
Should not have
• Should not use any color OTHER THAN black, silver, white or purple

```html
<!DOCTYPE html>
<html lang="en">
<head>
<meta charset="utf-8">
<title>Halden — Business Card</title>
<link rel="stylesheet" href="https://fonts.googleapis.com/css2?family=Cinzel:wght@400;600&family=Open+Sans:wght@400;600&display=swap">
<style>
  :root {
    --backdrop: #1a1a1b;
    --card-white: #ffffff;
    --card-black: #101011;
    --silver: #9c9ea4;
    --silver-light: #d4d6da;
    --silver-dark: #6f7176;
    --ink: #2b2b2b;
    --rule: #a3a3a3;
    --pattern-dark: #161617;
    --pattern-mid: #262628;
    --gloss: rgba(255, 255, 255, 0.07);
  }
  * { margin: 0; padding: 0; box-sizing: border-box; }
  html, body {
    width: 1200px; height: 871px; overflow: hidden;
    background: var(--backdrop);
  }
  .stage { position: relative; width: 1200px; height: 871px; }

  .card {
    position: absolute; left: 250px;
    width: 700px; height: 400px;
    border-radius: 28px; overflow: hidden;
  }

  /* Back side: layered black with embossed depth */
  .card--back {
    top: 25px;
    background: var(--card-black);
    box-shadow:
      inset 0 2px 0 rgba(255, 255, 255, 0.08),
      inset 0 -3px 6px rgba(0, 0, 0, 0.6),
      0 14px 30px rgba(0, 0, 0, 0.55);
  }
  .back-pattern {
    position: absolute; inset: 0;
    background:
      radial-gradient(ellipse at 30% 40%, var(--pattern-mid), transparent 60%),
      radial-gradient(ellipse at 75% 60%, var(--pattern-mid), transparent 55%),
      linear-gradient(135deg, var(--pattern-dark), #1d1d1f 50%, var(--pattern-dark));
  }
  .back-gloss {
    position: absolute; inset: 0;
    background: linear-gradient(160deg, var(--gloss) 0%, transparent 35%, transparent 65%, var(--gloss) 100%);
  }
  .back-brand {
    position: absolute; inset: 0;
    display: flex; flex-direction: column; align-items: center; justify-content: center; gap: 18px;
  }
  .brand-mark {
    width: 70px; height: 70px;
    background: linear-gradient(135deg, var(--silver-light), var(--silver) 55%, var(--silver-dark));
  }
  .brand-name {
    font-family: "Open Sans", sans-serif; font-weight: 600;
    font-size: 30px; letter-spacing: 4px; color: var(--silver);
  }

  /* Front side */
  .card--front {
    top: 446px; background: var(--card-white);
    box-shadow: 0 14px 30px rgba(0, 0, 0, 0.55);
  }
  .front-edge {
    position: absolute; left: 0; right: 0; bottom: 0; height: 14px;
    background: linear-gradient(90deg, var(--silver-dark), var(--silver-light) 40%, var(--silver) 70%, var(--silver-light));
  }
  .front-brand {
    position: absolute; left: 70px; top: 40px;
    display: flex; flex-direction: column; align-items: flex-start; gap: 12px;
  }
  .front-brand .brand-mark { width: 64px; height: 64px; margin-left: 18px; }
  .front-brand .brand-name { font-size: 24px; letter-spacing: 3px; }

  .divider {
    position: absolute; left: 90px; right: 40px; top: 222px;
    height: 1px; background: var(--rule);
  }
  .contact {
    position: absolute; left: 50px; top: 240px;
    list-style: none;
    font-family: "Open Sans", sans-serif; font-size: 13px;
    letter-spacing: 1.5px; color: var(--ink);
  }
  .contact li { display: flex; align-items: center; gap: 24px; height: 30px; }
  .contact svg { width: 14px; height: 14px; flex: none; }

  .person {
    position: absolute; right: 40px; top: 252px; text-align: right;
  }
  .person-name {
    font-family: "Cinzel", serif; font-weight: 400;
    font-size: 22px; letter-spacing: 4px; color: var(--ink);
  }
  .person-role {
    font-family: "Cinzel", serif; font-size: 13px;
    letter-spacing: 2px; color: var(--silver-dark); margin-top: 12px;
  }
  .person-rule {
    width: 360px; height: 1px; background: var(--rule);
    margin-top: 8px; margin-left: auto;
  }
</style>
</head>
<body>
<main class="stage">

  <section class="card card--back" aria-label="Card back">
    <div class="back-pattern" role="img" aria-label="Faint embossed tonal repeat of the brand symbol across the black card"></div>
    <div class="back-gloss"></div>
    <div class="back-brand">
      <div class="brand-mark"></div>
      <div class="brand-name">HALDEN</div>
    </div>
  </section>

  <section class="card card--front" aria-label="Card front">
    <div class="front-brand">
      <div class="brand-mark"></div>
      <div class="brand-name">HALDEN</div>
    </div>

    <div class="divider"></div>

    <ul class="contact">
      <li>
        <svg viewBox="0 0 16 16" aria-hidden="true"><path d="M2 6c0-2 3-3 6-3s6 1 6 3l-2 1-1-2H5L4 7 2 6zM4 8h8l1 5H3l1-5zm4 1.5a1.5 1.5 0 100 3 1.5 1.5 0 000-3z" fill="var(--silver-dark)"/></svg>
        <span>555-014-2290</span>
      </li>
      <li>
        <svg viewBox="0 0 16 16" aria-hidden="true"><rect x="1.5" y="3.5" width="13" height="9" fill="none" stroke="var(--silver-dark)" stroke-width="1.3"/><path d="M1.5 3.5l6.5 5 6.5-5" fill="none" stroke="var(--silver-dark)" stroke-width="1.3"/></svg>
        <span>vance.m.studio@example.com</span>
      </li>
    </ul>

    <div class="person">
      <div class="person-name">Mirela Vance, B.A.</div>
      <div class="person-role">Ceo</div>
      <div class="person-rule"></div>
    </div>

    <div class="front-edge"></div>
  </section>

</main>
</body>
</html>
```